Orthopedic Arm Surgeon Brochure

Bifold modern design. I will supply the text, my photo, and photos of my textbooks. Prefer colors in the greens, blues, greys. For more information visit LimbForwardClinic.com Please feel free to e-mail me with any questions. Current brochure attached; I want to modernize this, get rid of frames, and change the text.

Target Market(s)

High-end market

Colors
3176b5
33a6d7
33b8a4
abd036
876aae
b768aa

Requirements
Must have
• Beautiful finishes
Should not have
• Bright reds, yellows, oranges that emit fear

```html
<!DOCTYPE html>
<html lang="en">
<head>
<meta charset="utf-8">
<title>Lakeside Orthopedic Group – Hand &amp; Arm Surgery Brochure</title>
<link rel="stylesheet" href="https://fonts.googleapis.com/css2?family=Montserrat:wght@600;700;800&family=Open+Sans:wght@400;600;700&display=swap">
<style>
  :root{
    --blue:#3176b5;
    --sky:#33a6d7;
    --teal:#33b8a4;
    --green:#2fa88c;
    --purple:#876aae;
    --ink:#3b3f45;
    --muted:#5c636b;
    --paper:#ffffff;
    --mist:#eef0f3;
    --stage:#6a6c70;
  }
  *{box-sizing:border-box;margin:0;padding:0}
  html,body{width:1085px;height:1200px;overflow:hidden}
  body{background:var(--stage);font-family:"Open Sans",Arial,sans-serif;color:var(--ink);position:relative}

  .spread{position:absolute;left:20px;width:1045px;height:570px;display:flex;box-shadow:0 6px 18px rgba(0,0,0,.35)}
  .spread--outside{top:20px}
  .spread--inside{top:610px}
  .page{position:relative;width:522.5px;height:570px;overflow:hidden;background:var(--paper)}
  .page + .page{border-left:1px solid #d4d7db}
  .layer{position:absolute;inset:0;width:100%;height:100%}
  .placeholder{position:absolute}

  /* ---------- back cover ---------- */
  .back{background:linear-gradient(180deg,#f4f5f7 0%,#e2e5e9 45%)}
  .portrait{left:28px;top:38px;width:150px;height:176px;background:linear-gradient(160deg,#d9dde2 0%,#8a93a0 55%,#2f3642 100%)}
  .books{position:absolute;left:196px;top:26px;display:grid;grid-template-columns:repeat(3,72px);gap:10px}
  .book{height:92px;border:3px solid var(--blue)}
  .book--a{background:linear-gradient(150deg,#d7c59a,#8e7448)}
  .book--b{background:linear-gradient(150deg,#c8303b,#7a1b22)}
  .book--c{background:linear-gradient(150deg,#3a3f8c,#1f2250)}
  .book--d{background:linear-gradient(150deg,#b52c3a,#6c1720)}
  .book--e{background:linear-gradient(150deg,#5e86a8,#c9895a)}
  .book--f{background:linear-gradient(150deg,#2c2f6e,#7d3c8a)}

  .bio{position:absolute;left:30px;top:262px;width:462px;color:#fff;font-size:9.6px;line-height:1.42}
  .bio p{border-left:2px solid rgba(255,255,255,.85);padding-left:10px;margin-bottom:9px}
  .locations-title{position:absolute;left:30px;top:372px;width:470px;color:#fff;font-family:"Montserrat",sans-serif;font-weight:800;font-size:11.5px;letter-spacing:.2px}
  .locations{position:absolute;left:30px;top:396px;width:470px;display:grid;grid-template-columns:1fr 1fr;row-gap:12px;column-gap:16px}
  .location{display:flex;gap:9px;color:#fff;font-size:8.8px;line-height:1.35}
  .map{position:relative;flex:0 0 62px;height:46px;background:linear-gradient(135deg,#f3f1ea,#d9e3ea);border:1px solid rgba(255,255,255,.6)}
  .location h4{font-family:"Montserrat",sans-serif;font-weight:800;font-size:9.5px;text-transform:uppercase;margin-bottom:1px}

  .footer{position:absolute;left:0;right:0;display:flex;gap:22px;align-items:center;font-family:"Montserrat",sans-serif;font-weight:700;font-size:10px;color:#2d3a4a}
  .footer span{display:flex;align-items:center;gap:5px}
  .footer svg{width:11px;height:11px}
  .back .footer{top:528px;left:32px}
  .front .footer{top:526px;justify-content:center}

  /* ---------- front cover ---------- */
  .brand{position:absolute;left:160px;top:178px;width:202px;height:50px;border:3px solid var(--purple);border-radius:50%;background:#fff;display:flex;align-items:center;justify-content:center;gap:6px}
  .brand i{width:8px;height:8px;border-radius:50%;background:var(--blue)}
  .brand b{font-family:"Montserrat",sans-serif;font-weight:700;font-size:11.5px;color:var(--blue)}
  .rule{position:absolute;left:56px;right:56px;height:2px;background:var(--blue)}
  .title{position:absolute;left:0;right:0;top:258px;text-align:center}
  .title h1{font-family:"Montserrat",sans-serif;font-weight:800;font-size:29px;color:var(--green);letter-spacing:-.3px}
  .title h2{font-family:"Montserrat",sans-serif;font-weight:800;font-size:13px;color:#1f2a36;margin-top:3px}
  .title p{font-size:9.6px;font-weight:600;color:#2a333d;line-height:1.35}
  .services{position:absolute;top:362px;left:56px;right:56px;display:flex;justify-content:space-between;font-size:9.4px;color:#2a333d;line-height:1.62}
  .services ul{list-style:none}
  .services--left{text-align:right}
  .services--left li::after{content:"";display:inline-block;width:4px;height:4px;border-radius:50%;background:var(--teal);margin-left:6px;vertical-align:middle}
  .services--right li{padding-left:10px;position:relative}
  .services--right li::before{content:"";position:absolute;left:0;top:6px;width:4px;height:4px;border-radius:50%;background:var(--teal)}

  /* ---------- inside pages ---------- */
  .topic{position:absolute;left:28px;right:28px;display:flex;gap:16px;align-items:flex-start}
  .topic__text{flex:1}
  .topic__text p{font-size:8.9px;line-height:1.42;text-align:justify;color:var(--muted)}
  .tab{display:inline-flex;align-items:center;height:21px;padding:0 18px 0 16px;margin-bottom:6px;background:var(--teal);color:#fff;border-radius:0 11px 11px 0;font-family:"Montserrat",sans-serif;font-weight:800;font-size:10px;letter-spacing:.4px;text-transform:uppercase;position:relative}
  .tab::before{content:"";position:absolute;left:-6px;top:0;width:8px;height:21px;background:var(--blue);transform:skewX(-18deg)}
  .photo{flex:0 0 146px;height:96px;border:3px solid var(--sky);position:relative}
  .photo--cast{background:linear-gradient(150deg,#f4f5f7,#e9b7c9)}
  .photo--wrist{background:linear-gradient(150deg,#c9cfd6,#e8d2c4)}
  .photo--elbow{background:linear-gradient(150deg,#eef0f2,#d8c6b9)}
  .photo--forest{background:linear-gradient(150deg,#6f8a5c,#2e8f9a)}
  .photo--hand{background:linear-gradient(150deg,#f1ece6,#d7b8d6)}
  .photo--shoulder{background:linear-gradient(150deg,#9aa6b4,#c6a58b)}
</style>
</head>
<body>

<!-- Outside: back cover + front cover -->
<section class="spread spread--outside">

  <article class="page back">
    <svg class="layer" viewBox="0 0 522 570" preserveAspectRatio="none" aria-hidden="true">
      <path d="M0 248 Q260 222 522 196 V518 H0 Z" fill="var(--blue)"/>
      <path d="M0 246 Q260 220 522 194" fill="none" stroke="var(--purple)" stroke-width="2.5"/>
      <rect x="0" y="518" width="522" height="34" fill="#fff"/>
      <rect x="0" y="552" width="522" height="18" fill="var(--blue)"/>
    </svg>

    <div class="placeholder portrait" role="img" aria-label="Portrait photo of the surgeon in a dark suit"></div>
    <div class="books" role="img" aria-label="Covers of six textbooks edited by the surgeon">
      <div class="book book--a"></div><div class="book book--b"></div><div class="book book--c"></div>
      <div class="book book--d"></div><div class="book book--e"></div><div class="book book--f"></div>
    </div>

    <div class="bio">
      <p>Dr. Hollis is a nationally-recognized Upper Extremity Surgeon who has edited 7 textbooks, published over 45 original research papers and written 23 textbook chapters.</p>
      <p>Dr. Hollis graduated Cum Laude from Northfield University and with honors from Westbrook Medical School. He completed his residency in Orthopaedic Surgery at Coastal State University. In order to obtain expertise covering the entire upper extremity, he completed two fellowships, one in Hand Surgery and the other in Sports Medicine. He is board certified in Orthopaedic Surgery and has a Certificate of Additional Qualification in Hand Surgery.</p>
    </div>

    <h3 class="locations-title">DR. HOLLIS SEES PATIENTS AT THE FOLLOWING LOCATIONS:</h3>
    <div class="locations">
      <div class="location">
        <div class="map" role="img" aria-label="Street map of the Central Medical Campus location"></div>
        <div><h4>Central Medical Campus</h4>4200 Harbor Street<br>Suite 310<br>Riverton, TX 77001</div>
      </div>
      <div class="location">
        <div class="map" role="img" aria-label="Street map of the Millbrook location"></div>
        <div><h4>Millbrook</h4>7750 Lakeview Dr<br>Suite 120<br>Millbrook, TX 77003</div>
      </div>
      <div class="location">
        <div class="map" role="img" aria-label="Street map of the Westgate location"></div>
        <div><h4>Westgate</h4>218 Elm Grove Dr<br>Westgate, TX 77002</div>
      </div>
      <div class="location">
        <div class="map" role="img" aria-label="Street map of the Northpoint location"></div>
        <div><h4>Northpoint</h4>9315 Cedar Road West<br>Northpoint, TX 77004</div>
      </div>
    </div>

    <div class="footer">
      <span><svg viewBox="0 0 24 24"><path d="M6.6 10.8a15.1 15.1 0 0 0 6.6 6.6l2.2-2.2a1 1 0 0 1 1-.25 11.4 11.4 0 0 0 3.6.57 1 1 0 0 1 1 1V20a1 1 0 0 1-1 1A17 17 0 0 1 3 4a1 1 0 0 1 1-1h3.5a1 1 0 0 1 1 1c0 1.25.2 2.45.57 3.57a1 1 0 0 1-.25 1z" fill="#2d3a4a"/></svg>555-010-ARMS</span>
      <span><svg viewBox="0 0 24 24"><circle cx="12" cy="12" r="9" fill="none" stroke="#2d3a4a" stroke-width="2"/><path d="M3 12h18M12 3c3 3 3 15 0 18M12 3c-3 3-3 15 0 18" fill="none" stroke="#2d3a4a" stroke-width="1.6"/></svg>www.LimbForwardClinic.com</span>
    </div>
  </article>

  <article class="page front">
    <svg class="layer" viewBox="0 0 522 570" preserveAspectRatio="none" role="img" aria-label="Photo of a man running along a rocky beach under a blue sky">
      <defs>
        <linearGradient id="beach" x1="0" y1="0" x2="0" y2="1">
          <stop offset="0" stop-color="#2f6fb4"/>
          <stop offset=".55" stop-color="#9cc6e6"/>
          <stop offset=".75" stop-color="#4a7f9c"/>
          <stop offset="1" stop-color="#d8c7a6"/>
        </linearGradient>
      </defs>
      <path d="M0 0 H522 V150 Q300 218 0 178 Z" fill="url(#beach)"/>
      <rect x="0" y="552" width="522" height="18" fill="var(--blue)"/>
      <rect x="56" y="514" width="410" height="2" fill="var(--blue)"/>
    </svg>

    <div class="brand"><i></i><b>Lakeside Orthopedic Group</b></div>

    <div class="rule" style="top:246px"></div>
    <header class="title">
      <h1>Daniel R. Hollis, MD</h1>
      <h2>Specialist in Surgery of the</h2>
      <p>Hand, Wrist, Elbow &amp; Shoulder Board Certified Orthopedic Surgeon</p>
      <p>Certificate of Additional Qualification, Hand Surgery</p>
    </header>
    <div class="rule" style="top:348px"></div>

    <div class="services">
      <ul class="services--left">
        <li>Endoscopic Carpal Tunnel Release</li>
        <li>Endoscopic Cubital Tunnel Release</li>
        <li>Trigger Finger Release</li>
        <li>Tendon and Nerve Repairs</li>
        <li>Hand &amp; Wrist Pain</li>
        <li>Sports Injuries</li>
        <li>Fractures</li>
      </ul>
      <ul class="services--right">
        <li>Dislocations</li>
        <li>Arthritis</li>
        <li>Wrist, Elbow &amp; Shoulder Arthroscopy</li>
        <li>Tennis Elbow</li>
        <li>Arthroscopic Rotator Cuff Repairs</li>
        <li>Fellowship Trained in Sports Medicine</li>
      </ul>
    </div>

    <div class="footer">
      <span><svg viewBox="0 0 24 24"><path d="M6.6 10.8a15.1 15.1 0 0 0 6.6 6.6l2.2-2.2a1 1 0 0 1 1-.25 11.4 11.4 0 0 0 3.6.57 1 1 0 0 1 1 1V20a1 1 0 0 1-1 1A17 17 0 0 1 3 4a1 1 0 0 1 1-1h3.5a1 1 0 0 1 1 1c0 1.25.2 2.45.57 3.57a1 1 0 0 1-.25 1z" fill="#2d3a4a"/></svg>555-010-ARMS</span>
      <span><svg viewBox="0 0 24 24"><circle cx="12" cy="12" r="9" fill="none" stroke="#2d3a4a" stroke-width="2"/><path d="M3 12h18M12 3c3 3 3 15 0 18M12 3c-3 3-3 15 0 18" fill="none" stroke="#2d3a4a" stroke-width="1.6"/></svg>www.LimbForwardClinic.com</span>
    </div>
  </article>
</section>

<!-- Inside spread -->
<section class="spread spread--inside">

  <article class="page inner">
    <svg class="layer" viewBox="0 0 522 570" preserveAspectRatio="none" aria-hidden="true">
      <path d="M0 0 H522 V22 Q260 44 0 30 Z" fill="var(--sky)"/>
      <path d="M0 34 Q260 48 522 26" fill="none" stroke="var(--blue)" stroke-width="2"/>
      <path d="M0 570 H522 V548 Q260 528 0 544 Z" fill="var(--sky)"/>
      <path d="M0 540 Q260 524 522 544" fill="none" stroke="var(--blue)" stroke-width="2"/>
    </svg>

    <div class="topic" style="top:54px">
      <div class="topic__text">
        <span class="tab">Finger &amp; Hand Fractures</span>
        <p>Fractures (breaks) of the hand and fingers are very common. These fractures heal very quickly, often within 3 weeks. If not treated within that time frame, the fracture can heal in poor position, often compromising hand function. Many think "it's just a sprain," yet often only an X-ray can tell for sure. If the fragments have moved, surgery may be needed. The sooner the fracture is treated, the quicker motion can start and the less permanent stiffness will occur.</p>
      </div>
      <div class="photo photo--cast" role="img" aria-label="Photo of a hand and wrist in a pink cast"></div>
    </div>

    <div class="topic" style="top:218px">
      <div class="topic__text">
        <span class="tab">Wrist Fractures</span>
        <p>The large bone of the wrist, the distal radius, is the most commonly broken bone in the body. If the fracture hasn't been displaced it may heal in a cast; if significant displacement has occurred, it is best treated with fixation using a plate. The scaphoid, one of the small wrist bones, often fails to heal and can collapse, leading to pain and arthritis. Because these fractures often aren't visible on early X-rays, a cast or an MRI is used so none are missed.</p>
      </div>
      <div class="photo photo--wrist" role="img" aria-label="Photo of a person holding a painful wrist"></div>
    </div>

    <div class="topic" style="top:388px">
      <div class="topic__text">
        <span class="tab">Elbow Fractures</span>
        <p>The elbow is a commonly fractured joint. The elbow is prone to stiffness and many of its fractures are part of highly complex injury patterns involving multiple fractures and ligament injuries. If not treated in a timely fashion, permanent stiffness and dysfunction may result. These injuries are best treated by orthopedic specialists with experience fixing elbow fractures and ligament injuries.</p>
      </div>
      <div class="photo photo--elbow" role="img" aria-label="Photo of a bandaged elbow"></div>
    </div>
  </article>

  <article class="page inner">
    <svg class="layer" viewBox="0 0 522 570" preserveAspectRatio="none" aria-hidden="true">
      <path d="M0 0 H522 V30 Q260 44 0 22 Z" fill="var(--sky)"/>
      <path d="M0 26 Q260 48 522 34" fill="none" stroke="var(--blue)" stroke-width="2"/>
      <path d="M0 570 H522 V544 Q260 528 0 548 Z" fill="var(--sky)"/>
      <path d="M0 544 Q260 524 522 540" fill="none" stroke="var(--blue)" stroke-width="2"/>
    </svg>

    <div class="topic" style="top:54px">
      <div class="topic__text">
        <span class="tab">Flexor Tendon Lacerations</span>
        <p>Tendon injuries can be devastating, life-changing events. The flexor tendons are the rope-like structures that bend the fingers and thumb. They run through tight tunnels, so there's little room for swelling or scar tissue. Once cut, a flexor tendon retracts and must be repaired quickly, ideally within days. The repaired tendon can stick in the tunnel, so hand therapy after surgery is just as important as the surgery itself. Surgery will not succeed without it.</p>
      </div>
      <div class="photo photo--forest" role="img" aria-label="Photo of a woman sitting in a forest holding her hand"></div>
    </div>

    <div class="topic" style="top:218px">
      <div class="topic__text">
        <span class="tab">Nerve Lacerations</span>
        <p>Nerve lacerations lead to numbness of the fingers. If a nerve in the finger or hand is cut, it needs to be repaired in order to regain sensation at the fingertip. Timing is not as critical as for tendon injuries. Most sharp nerve lacerations are best repaired directly. Crush or larger injuries may require removing the injured area of nerve and placing the cut ends into an absorbable tube so they can heal together.</p>
      </div>
      <div class="photo photo--hand" role="img" aria-label="Photo of a woman holding her sore hand"></div>
    </div>

    <div class="topic" style="top:388px">
      <div class="topic__text">
        <span class="tab">Rotator Cuff Tears</span>
        <p>The rotator cuff is made up of the tendons that elevate the shoulder. Rotator cuff tears result in significant pain. If the tear is large, the ability to elevate the arm may be lost. If the rotator cuff is torn due to a fall or other trauma, function and pain relief are best restored through surgery. Rotator cuff tears can be repaired arthroscopically as an outpatient procedure, with less pain and stiffness than traditional techniques.</p>
      </div>
      <div class="photo photo--shoulder" role="img" aria-label="Photo of a woman holding her painful shoulder"></div>
    </div>
  </article>
</section>

</body>
</html>
```